KB Rubbish Removal Business Card

Hey,
I need a double sided business card designed for a rubbish removal business based in Australia. Logo is already chosen, similar colours preferred for both sides of the business card.

Details to include:

Front:

KB Rubbish Removal
Darren Holloway
Managing Director
Mobile: 0471 902 146
Email: darren@kbrubbishremoval.com.au
Website: kbrubbishremoval.com.au

Rear:

How did we do?
kbrubbishremoval.com.au/review

```html
<!DOCTYPE html>
<html lang="en">
<head>
<meta charset="utf-8">
<title>KB Rubbish Removal Business Card</title>
<link href="https://fonts.googleapis.com/css2?family=Open+Sans:wght@400;600;700&display=swap" rel="stylesheet">
<style>
  :root {
    --backdrop: #3b3b3c;
    --paper: #ffffff;
    --brand-green: #16823f;
    --bright-green: #3bb54a;
    --ink: #1d1d1b;
    --silver: #d2d3d5;
  }
  * { margin: 0; padding: 0; box-sizing: border-box; }
  html, body {
    width: 1200px; height: 1059px; overflow: hidden;
    background: var(--backdrop);
    font-family: "Open Sans", Arial, sans-serif;
  }
  .canvas { position: relative; width: 1200px; height: 1059px; }
  .card {
    position: absolute; width: 690px; height: 392px; overflow: hidden;
  }
  .card--front { left: 255px; top: 100px; background: var(--paper); }
  .card--back { left: 254px; top: 537px; background: var(--brand-green); }

  .wave { position: absolute; inset: 0; width: 690px; height: 392px; }

  .name-tab {
    position: absolute; left: -4px; top: 88px; width: 15px; height: 39px;
    background: var(--brand-green); border-radius: 3px;
  }
  .holder { position: absolute; left: 28px; top: 84px; }
  .holder__name {
    font-weight: 700; font-size: 26px; line-height: 30px;
    color: var(--brand-green); letter-spacing: 0.2px;
  }
  .holder__role { font-size: 17px; line-height: 20px; color: var(--ink); }

  .brand {
    position: absolute; left: 372px; top: 46px; width: 300px;
    display: flex; flex-direction: column; align-items: center;
  }
  .brand__dot {
    width: 108px; height: 108px; border-radius: 50%;
    background: var(--bright-green);
  }
  .brand__name {
    margin-top: 16px; text-align: center;
    font-weight: 700; font-size: 32px; line-height: 34px;
    color: var(--brand-green); text-transform: uppercase;
  }

  .contacts {
    position: absolute; left: 28px; top: 302px; list-style: none;
    color: var(--paper); font-size: 17px; line-height: 21.5px;
  }
  .contacts li { display: flex; align-items: center; }
  .contacts svg { width: 11px; height: 11px; margin-right: 7px; fill: var(--paper); flex: none; }

  .back-brand {
    position: absolute; inset: 0;
    display: flex; flex-direction: column; align-items: center; justify-content: center;
  }
  .back-brand__dot {
    width: 130px; height: 130px; border-radius: 50%; background: var(--silver);
  }
  .back-brand__name {
    margin-top: 16px; font-weight: 700; font-size: 28px; line-height: 32px;
    color: var(--silver); text-transform: uppercase;
  }
  .review { margin-top: 18px; text-align: center; color: var(--paper); }
  .review__ask { font-weight: 600; font-size: 20px; line-height: 26px; }
  .review__link { font-size: 17px; line-height: 22px; }
</style>
</head>
<body>
<div class="canvas">
  <section class="card card--front">
    <svg class="wave" viewBox="0 0 690 392" aria-hidden="true">
      <path fill="#3bb54a" d="M0,258 C60,220 120,208 170,208 C290,208 400,334 560,334 C620,334 662,328 690,313 V392 H0Z"/>
      <path fill="#ffffff" d="M0,268 C60,230 110,217 160,217 C280,217 390,339 560,339 C620,339 660,333 690,320 V392 H0Z"/>
      <path fill="#16823f" d="M0,273 C60,235 110,222 160,222 C280,222 390,344 560,344 C620,344 660,338 690,325 V392 H0Z"/>
    </svg>

    <div class="name-tab"></div>
    <div class="holder">
      <p class="holder__name">Darren Holloway</p>
      <p class="holder__role">Managing Director</p>
    </div>

    <div class="brand">
      <div class="brand__dot"></div>
      <p class="brand__name">KB Rubbish<br>Removal</p>
    </div>

    <ul class="contacts">
      <li>
        <svg viewBox="0 0 24 24"><path d="M6.6 10.8a15 15 0 0 0 6.6 6.6l2.2-2.2a1 1 0 0 1 1-.25 11.4 11.4 0 0 0 3.6.6 1 1 0 0 1 1 1V20a1 1 0 0 1-1 1A17 17 0 0 1 3 4a1 1 0 0 1 1-1h3.5a1 1 0 0 1 1 1c0 1.25.2 2.45.6 3.6a1 1 0 0 1-.25 1z"/></svg>
        0471 902 146
      </li>
      <li>
        <svg viewBox="0 0 24 24"><path d="M2 5h20v14H2z M3 6l9 7 9-7" stroke="#16823f" stroke-width="1.5"/></svg>
        darren@kbrubbishremoval.com.au
      </li>
      <li>
        <svg viewBox="0 0 24 24"><circle cx="12" cy="12" r="10"/><path d="M7 6c2 1 2 3 4 3s1 3-1 4-1 4-2 5M15 4c-1 2 1 3 3 3M17 14c-2 0-3 2-2 4" stroke="#16823f" stroke-width="2" fill="none"/></svg>
        kbrubbishremoval.com.au
      </li>
    </ul>
  </section>

  <section class="card card--back">
    <div class="back-brand">
      <div class="back-brand__dot"></div>
      <p class="back-brand__name">KB Rubbish Removal</p>
      <div class="review">
        <p class="review__ask">How did we do?</p>
        <p class="review__link">kbrubbishremoval.com.au/review</p>
      </div>
    </div>
  </section>
</div>
</body>
</html>
```